Graniteway Surface Works, Inc. Business Card

New business, we do epoxy, polishing concrete, underlayment, fluid applied flooring, sound proofing, double sided, will need 3 sets of cards with 3 different names and phone numbers.
Company: Graniteway Surface Works, Inc.
Address and Phone: 6339 Charlotte Pike PMB 2183Nashville, TN 38514
(615) 418-3927
www.granitewaysurfaceworks.example

Target Market(s)

General Contractors, Contractors, Architects

Contact Information for Business Card

1st Card: Devon Halvorsen C. 708.214.5873 e. devon@granitewaysurfaceworks.example
Vice President
2nd Card: Morgan Prescoe C. 708.389.6145 e. morgan@granitewaysurfaceworks.example
President
3rd Card: Bo Vu C. 405.631.8207 e. bo@granitewaysurfaceworks.example
Managing Partner

Font styles to use
Serif
Sans Serif

Requirements
Must have
• Professional Clean Design, Implement colors from Logo or nicely contrasting
Nice to have
• N/A

```html
<!DOCTYPE html>
<html lang="en">
<head>
<meta charset="utf-8">
<title>Graniteway Surface Works – Business Card</title>
<link rel="stylesheet" href="https://fonts.googleapis.com/css2?family=Montserrat:wght@400;700&display=swap">
<style>
  :root {
    --backdrop: #2b2b2b;
    --brand-blue: #0763b0;
    --brand-green: #6ba14c;
    --ink: #231f20;
    --paper: #ffffff;
  }
  * { box-sizing: border-box; margin: 0; padding: 0; }
  html, body { width: 1200px; height: 1015px; overflow: hidden; }
  body {
    background: var(--backdrop);
    font-family: "Montserrat", sans-serif;
    position: relative;
  }
  .card {
    position: absolute;
    width: 700px;
    height: 400px;
    left: 250px;
    box-shadow: 0 10px 28px rgba(0,0,0,.5);
    overflow: hidden;
  }
  .card--front { top: 78px; background: var(--brand-blue); padding: 26px 40px; }
  .card--back  { top: 538px; background: var(--paper); }

  .front-panel {
    width: 100%; height: 100%;
    background: var(--paper);
    display: flex; align-items: center; justify-content: center; gap: 14px;
  }
  .wordmark-square { width: 22px; height: 22px; background: var(--brand-green); }
  .wordmark {
    font-weight: 700;
    font-size: 27px;
    letter-spacing: .04em;
    color: var(--ink);
    text-transform: uppercase;
  }

  .back-info {
    position: absolute; left: 0; top: 0; bottom: 0; width: 400px;
    background: var(--brand-green);
    color: var(--paper);
    padding: 58px 0 0 58px;
  }
  .floor-pattern {
    position: absolute; right: 0; top: 0; bottom: 0; width: 300px;
    background: linear-gradient(135deg, #ffffff 0%, #c9dfbb 45%, #8fbc73 100%);
  }
  .contact-list { list-style: none; }
  .contact-list li {
    display: flex; align-items: center; gap: 12px;
    font-size: 15px; line-height: 27px; white-space: nowrap;
  }
  .contact-list svg { width: 15px; height: 15px; flex: none; }
  .address { margin-top: 22px; font-size: 15px; line-height: 22px; padding-left: 27px; }
  .person { margin-top: 30px; padding-left: 27px; }
  .person-name { font-weight: 700; font-size: 21px; text-transform: uppercase; letter-spacing: .01em; }
  .person-title { font-size: 16px; margin-top: 2px; }
</style>
</head>
<body>

<section class="card card--front" aria-label="Business card front">
  <div class="front-panel">
    <span class="wordmark-square"></span>
    <span class="wordmark">Graniteway Surface Works</span>
  </div>
</section>

<section class="card card--back" aria-label="Business card back">
  <div class="back-info">
    <ul class="contact-list">
      <li>
        <svg viewBox="0 0 16 16" fill="none" stroke="currentColor" stroke-width="1.6"><rect x="4" y="1.5" width="8" height="13" rx="1.2"/><line x1="7" y1="12" x2="9" y2="12"/></svg>
        708.214.5873
      </li>
      <li>
        <svg viewBox="0 0 16 16" fill="none" stroke="currentColor" stroke-width="1.6"><path d="M3 2.5l3 .5 1 3-1.6 1.2a8 8 0 0 0 3.4 3.4L10 9l3 1 .5 3c-.5 1-1.5 1.5-2.5 1.5A10 10 0 0 1 1.5 5c0-1 .5-2 1.5-2.5z"/></svg>
        (615) 418-3927
      </li>
      <li>
        <svg viewBox="0 0 16 16" fill="none" stroke="currentColor" stroke-width="1.6"><rect x="1.5" y="3.5" width="13" height="9"/><path d="M1.5 3.5L8 9l6.5-5.5"/></svg>
        devon@granitewaysurfaceworks.example
      </li>
      <li>
        <svg viewBox="0 0 16 16" fill="none" stroke="currentColor" stroke-width="1.4"><circle cx="8" cy="8" r="6.5"/><ellipse cx="8" cy="8" rx="2.8" ry="6.5"/><line x1="1.5" y1="8" x2="14.5" y2="8"/></svg>
        www.granitewaysurfaceworks.example
      </li>
    </ul>
    <p class="address">4812 Wendover Ridge<br>PMB 7416 Nashville, TN 38514</p>
    <div class="person">
      <p class="person-name">Devon Halvorsen</p>
      <p class="person-title">Vice President</p>
    </div>
  </div>
  <div class="floor-pattern" role="img" aria-label="Green tiled floor grid receding in perspective"></div>
</section>

</body>
</html>
```